QR100 Quill Rover devices for home automaton systems

Graphic design/layout required for small cardboard box that will hold the Quill Rover device. A wireless/automatic internet of things device with a whimsical flair. Music box in clear plastic enclosure with spinning flag used for alerts in home automation system; someone is at the door, it automatically plays tune and spins flag. (garage door open alert/notification, someone at pool gate, etc.) large selection of tunes available. This is a battery powered wireless device with a mechanical music box that integrates into standard home automation systems. It acts as an automatic alert or notification device that is meant to less annoying/harsh than typical beeps or smartphone alerts.
See demo video: https://www.vidloomer.net/watch?feature=player_embedded&v=Kp3tQz8Rbnm

Target Market(s)

Automated Home Owners

Industry/Entity Type

Internet

Requirements
Must have
• Graphics/photo that integrates the flashing light and spinning flag as part of the design. Window to show working music drum, small window to show flashing led
Nice to have
• large window on one slide for custom slide in photo or graphics

```html
<!DOCTYPE html>
<html lang="en">
<head>
<meta charset="utf-8">
<title>Quill Rover – Box Dieline</title>
<link rel="stylesheet" href="https://fonts.googleapis.com/css2?family=Alfa+Slab+One&family=Roboto+Condensed:wght@700&display=swap">
<style>
  :root {
    --stage: #eceef0;
    --blue: #1f5ba8;
    --blue-deep: #174a8c;
    --sky: #9fd2ef;
    --red: #d21f2b;
    --white: #ffffff;
    --pole: #a7adb3;
    --led: #5fa8ff;
  }
  html, body { margin: 0; padding: 0; overflow: hidden; }
  body { width: 1200px; height: 1200px; background: var(--stage); }
  .dieline { display: block; width: 1200px; height: 1200px; }
  .fill-blue { fill: var(--blue); }
  .fill-sky { fill: var(--sky); }
  .fill-red { fill: var(--red); }
  .fill-white { fill: var(--white); }
  .pole { stroke: var(--pole); stroke-width: 6; }
  .rule { stroke: var(--sky); stroke-width: 4; }
  .fold { stroke: rgba(0,0,0,.18); stroke-width: 1; stroke-dasharray: 6 5; fill: none; }
  .product-name { font-family: "Alfa Slab One", Georgia, serif; font-size: 34px; fill: var(--white); letter-spacing: 1px; }
  .spec { font-family: "Roboto Condensed", Arial, sans-serif; font-weight: 700; font-size: 16px; fill: var(--white); }
  .spec-rule { stroke: var(--white); stroke-width: 1.5; }
  .tune-pill { fill: var(--blue); stroke: var(--white); stroke-width: 2; }
  .tune-label { font-family: "Roboto Condensed", Arial, sans-serif; font-weight: 700; font-size: 18px; fill: var(--white); }
  .brand-name { font-family: "Roboto Condensed", Arial, sans-serif; font-weight: 700; font-size: 22px; fill: var(--blue-deep); }
  .tagline { font-family: "Roboto Condensed", Arial, sans-serif; font-weight: 700; font-size: 12px; fill: var(--blue-deep); }
  .led-glow { fill: var(--led); }
  .led-window { fill: #10306a; }
</style>
</head>
<body>
<svg class="dieline" viewBox="0 0 1200 1200" xmlns="http://www.w3.org/2000/svg">
  <defs>
    <linearGradient id="canopyTone" x1="0" y1="0" x2="0" y2="1">
      <stop offset="0" stop-color="#1f5ba8"/>
      <stop offset=".45" stop-color="#5f9bd3"/>
      <stop offset="1" stop-color="#9fd2ef"/>
    </linearGradient>
    <linearGradient id="horseTone" x1="0" y1="0" x2="1" y2="1">
      <stop offset="0" stop-color="#fbf6e6"/>
      <stop offset=".55" stop-color="#f4e7b8"/>
      <stop offset="1" stop-color="#d9e6a0"/>
    </linearGradient>
    <radialGradient id="ledHalo">
      <stop offset="0" stop-color="#ffffff"/>
      <stop offset=".35" stop-color="#8cc4ff"/>
      <stop offset="1" stop-color="#5fa8ff" stop-opacity="0"/>
    </radialGradient>
  </defs>

  <!-- top lid flap -->
  <g class="lid">
    <path d="M85 260 V170 Q85 150 105 150 H365 Q385 150 385 170 V260 Z" class="fill-blue"/>
    <path d="M160 150 V120 Q160 108 172 108 H298 Q310 108 310 120 V150 Z" class="fill-blue"/>
  </g>

  <!-- spinning flag -->
  <g class="flag">
    <path d="M905 125 L985 150 L905 175 Z" class="fill-red"/>
    <path d="M928 140 l3.5 7 7.5 .8 -5.6 5 1.6 7.4 -7 -3.8 -7 3.8 1.6 -7.4 -5.6 -5 7.5 -.8 Z" class="fill-white"/>
  </g>

  <!-- canopy band -->
  <rect x="85" y="260" width="1000" height="60" fill="url(#canopyTone)" role="img" aria-label="Carousel canopy trim in blue and sky blue"/>
  <line x1="85" y1="321" x2="1085" y2="321" class="rule"/>
  <rect x="85" y="322" width="1000" height="28" class="fill-red" role="img" aria-label="Red carousel trim band"/>
  <line x1="85" y1="352" x2="1085" y2="352" class="rule"/>

  <!-- music drum window: carousel stripes -->
  <g class="carousel-stripes">
    <rect x="85" y="354" width="100" height="368" class="fill-white"/>
    <rect x="185" y="354" width="100" height="368" class="fill-blue"/>
    <rect x="285" y="354" width="100" height="368" class="fill-red"/>
    <rect x="385" y="354" width="100" height="368" class="fill-white"/>
    <rect x="485" y="354" width="100" height="368" class="fill-blue"/>
    <rect x="585" y="354" width="100" height="368" class="fill-red"/>
    <rect x="685" y="354" width="100" height="368" class="fill-white"/>
    <rect x="785" y="354" width="100" height="368" class="fill-blue"/>
    <rect x="885" y="354" width="100" height="368" class="fill-red"/>
    <rect x="985" y="354" width="100" height="368" class="fill-white"/>
  </g>
  <g class="carousel-poles">
    <line x1="185" y1="354" x2="185" y2="722" class="pole"/>
    <line x1="285" y1="354" x2="285" y2="722" class="pole"/>
    <line x1="485" y1="354" x2="485" y2="722" class="pole"/>
    <line x1="685" y1="354" x2="685" y2="722" class="pole"/>
    <line x1="785" y1="354" x2="785" y2="722" class="pole"/>
    <line x1="985" y1="354" x2="985" y2="722" class="pole"/>
  </g>
  <g class="carousel-horses">
    <rect x="105" y="470" width="150" height="170" rx="40" fill="url(#horseTone)" role="img" aria-label="Carousel horse with golden mane and green saddle"/>
    <rect x="230" y="400" width="150" height="170" rx="40" fill="url(#horseTone)" role="img" aria-label="Carousel horse with golden mane and green saddle"/>
    <rect x="420" y="430" width="140" height="170" rx="40" fill="url(#horseTone)" role="img" aria-label="Carousel horse with golden mane and green saddle"/>
    <rect x="605" y="400" width="150" height="170" rx="40" fill="url(#horseTone)" role="img" aria-label="Carousel horse with golden mane and green saddle"/>
    <rect x="730" y="480" width="150" height="170" rx="40" fill="url(#horseTone)" role="img" aria-label="Carousel horse with golden mane and green saddle"/>
    <rect x="920" y="440" width="140" height="170" rx="40" fill="url(#horseTone)" role="img" aria-label="Carousel horse with golden mane and green saddle"/>
  </g>

  <line x1="85" y1="723" x2="1085" y2="723" class="rule"/>
  <rect x="85" y="724" width="1000" height="51" class="fill-red" role="img" aria-label="Red base band with sound openings"/>

  <!-- LED window -->
  <circle cx="306" cy="749" r="8" class="led-window"/>
  <circle cx="306" cy="749" r="20" fill="url(#ledHalo)"/>
  <circle cx="306" cy="749" r="5" class="led-glow"/>

  <rect x="85" y="775" width="1000" height="185" class="fill-blue"/>

  <!-- front panel -->
  <text x="235" y="880" text-anchor="middle" class="product-name">QUILL ROVER</text>

  <!-- info side panel -->
  <g class="spec-block">
    <text x="485" y="828" text-anchor="middle" class="spec">Model: QR100</text>
    <text x="485" y="850" text-anchor="middle" class="spec">Batteries: 2XAAA</text>
    <line x1="415" y1="862" x2="555" y2="862" class="spec-rule"/>
    <text x="485" y="884" text-anchor="middle" class="spec">Brightwell Controls</text>
    <text x="485" y="904" text-anchor="middle" class="spec">A Div. of Halden Control Inc.</text>
  </g>

  <!-- back panel -->
  <text x="735" y="880" text-anchor="middle" class="product-name">QUILL ROVER</text>

  <!-- tune side panel -->
  <g class="tune-block">
    <rect x="925" y="808" width="120" height="34" rx="17" class="tune-pill"/>
    <text x="985" y="831" text-anchor="middle" class="tune-label">Tune Names</text>
  </g>

  <!-- glue flap -->
  <path d="M1085 270 L1115 290 V930 L1085 950 Z" class="fill-blue"/>

  <!-- bottom flap with maker -->
  <g class="base-flap">
    <path d="M85 960 H385 V1060 Q385 1080 365 1080 H105 Q85 1080 85 1060 Z" class="fill-sky"/>
    <rect x="110" y="990" width="34" height="34" class="fill-blue"/>
    <text x="154" y="1016" class="brand-name">Brightwell</text>
    <text x="110" y="1050" class="tagline">Smart Home Alert Devices &amp; Solutions</text>
  </g>

  <!-- fold lines -->
  <g class="folds">
    <line x1="85" y1="260" x2="385" y2="260" class="fold"/>
    <line x1="85" y1="960" x2="385" y2="960" class="fold"/>
    <line x1="385" y1="260" x2="385" y2="960" class="fold"/>
    <line x1="585" y1="260" x2="585" y2="960" class="fold"/>
    <line x1="885" y1="260" x2="885" y2="960" class="fold"/>
    <line x1="1085" y1="260" x2="1085" y2="960" class="fold"/>
  </g>
</svg>
</body>
</html>
```